Hollow Briar Flower Shop Jumbo Postcard

We are opening a new flower shop in a small southern town. Our style is a bit different than the traditional flower shop. We are specializing in garden wild floral bouquets and arrangements. We will offer a frequent flower program, roses for a month promotion. We are offering a free gift with any in store purchase. We are looking for a design that reflects our logo and its' colors and the focus on using foraged and natural elements in our work. We want to provide a product that stands out from the rest and that grabs your attention and makes people ask where did that come from?? We will supply flowers for all occasions, event planning, and one of a kind home décor items. We will have special start up offers of free local delivery to the first 30 customers mentioning the postcard offer, and special flower happy hour specials each day week. Finally I want to convey that we are new, we are different, and ready to serve our local community. We love rustic and shabby chic designs. . I want to postcard offers to stand out and grab the recipients' attention. It should include our contact info and website, what we provide, and our tagline from the business card.
Industry/Entity Type
Floral

```html
<!DOCTYPE html>
<html lang="en">
<head>
<meta charset="utf-8">
<title>Hollow Briar Flower Shop – Grand Opening Postcard</title>
<link rel="stylesheet" href="https://fonts.googleapis.com/css2?family=Cinzel:wght@400;700&family=Playball&family=Cabin+Condensed:wght@400;600;700&family=Shadows+Into+Light+Two&family=Quicksand:wght@400;500&family=Cabin:wght@600;700&family=Fjalla+One&display=swap">
<style>
  :root {
    --stage: #ece7dd;
    --paper: #f3ebcd;
    --paper-deep: #eadfb8;
    --orange: #e8714a;
    --slate: #8fabaa;
    --plum: #6a2c6c;
    --rose-red: #d8504a;
    --ink: #3b3838;
    --ink-soft: #5a5552;
    --rule: #9c9c9c;
    --white: #ffffff;
  }
  * { box-sizing: border-box; margin: 0; padding: 0; }
  html, body { width: 1200px; height: 500px; overflow: hidden; }
  body { background: var(--stage); position: relative; font-family: "Cabin Condensed", sans-serif; color: var(--ink); }

  .card { position: absolute; top: 33px; width: 568px; height: 432px; overflow: hidden; }
  .card--front { left: 22px; background: var(--paper); }
  .card--back { left: 612px; background: var(--white); }

  /* Front */
  .flower-strip { position: absolute; left: 0; top: 0; width: 118px; height: 432px;
    background: linear-gradient(180deg, #e9783c 0%, #6b2f7a 22%, #e46d2f 45%, #4a2660 65%, #e97a3d 80%, #5b2a6e 100%); }
  .opening-banner { position: absolute; left: 66px; top: 30px; width: 420px; height: 100px; }
  .opening-banner__title { position: absolute; left: 0; right: 0; top: 22px; text-align: center;
    font-family: "Cinzel", serif; font-size: 40px; color: var(--white); letter-spacing: 1px; line-height: 1; }
  .opening-banner__date { position: absolute; left: 0; right: 0; top: 64px; text-align: center;
    font-family: "Playball", cursive; font-size: 24px; color: #5e4f70; line-height: 1; }
  .tagline { position: absolute; left: 130px; top: 139px; font-size: 21px; color: var(--ink); }

  .brand-mark { position: absolute; left: 140px; top: 170px; width: 190px; height: 190px; }
  .brand-mark__name { position: absolute; left: 0; right: 0; top: 70px; text-align: center;
    font-family: "Cabin", sans-serif; font-weight: 600; font-size: 24px; line-height: 1.1; color: var(--ink-soft); }

  .service-note { position: absolute; left: 335px; top: 192px; width: 218px; text-align: right;
    font-family: "Shadows Into Light Two", cursive; font-size: 19px; line-height: 1.25; color: var(--ink-soft); }
  .gift-offer { position: absolute; left: 351px; top: 255px; width: 197px; height: 98px;
    border: 3px dashed var(--rose-red); text-align: center; font-family: "Cabin Condensed", sans-serif;
    font-weight: 700; font-size: 24px; line-height: 1.15; color: var(--ink-soft); padding-top: 6px; }
  .gift-offer__lead { color: var(--rose-red); display: block; }
  .phone { position: absolute; left: 354px; top: 358px; font-family: "Cabin Condensed", sans-serif;
    font-weight: 700; font-size: 25px; color: var(--rose-red); display: flex; align-items: center; gap: 4px; }
  .web-band { position: absolute; left: 118px; right: 0; bottom: 0; height: 46px; background: var(--paper-deep);
    text-align: center; font-family: "Cabin", sans-serif; font-weight: 700; font-size: 26px;
    color: var(--plum); line-height: 46px; letter-spacing: 0.5px; }

  /* Back */
  .offer-panel { position: absolute; left: 0; top: 0; width: 268px; height: 350px; background: var(--paper); }
  .offer-panel__intro { position: absolute; left: 30px; right: 30px; top: 10px; text-align: center;
    font-family: "Quicksand", sans-serif; font-size: 13px; line-height: 1.3; color: var(--ink-soft); }
  .products { position: absolute; left: 14px; top: 66px; font-family: "Quicksand", sans-serif;
    font-size: 12.5px; line-height: 17px; color: var(--ink-soft); }
  .products__list { list-style: none; }
  .products__list li::before { content: "\2733"; color: var(--orange); margin-right: 2px; font-size: 11px; }
  .delivery-heart { position: absolute; left: 12px; top: 194px; width: 112px; height: 86px; }
  .delivery-heart__text { position: absolute; left: 10px; right: 10px; top: 8px; text-align: center; color: var(--white);
    font-family: "Cabin Condensed", sans-serif; font-weight: 700; font-size: 8px; line-height: 1.15; }
  .delivery-heart__text strong { display: block; font-family: "Fjalla One", sans-serif; font-size: 22px; color: #6a2530; line-height: 1; }
  .frequent-program { position: absolute; left: 10px; top: 282px; width: 118px; text-align: center;
    font-family: "Fjalla One", sans-serif; font-size: 13px; line-height: 1.3; color: var(--rose-red); }
  .happy-hour { position: absolute; left: 137px; top: 203px; width: 118px; height: 74px; border: 4px solid #eb9163;
    border-radius: 10px; background: var(--paper); text-align: center; font-family: "Quicksand", sans-serif;
    font-weight: 500; font-size: 13px; line-height: 1.2; color: var(--ink); padding-top: 4px; }
  .rose-promo { position: absolute; left: 134px; top: 284px; width: 126px; text-align: center;
    font-family: "Cabin Condensed", sans-serif; font-weight: 700; font-size: 14px; line-height: 1.25; color: var(--ink); }

  .back-mark { position: absolute; left: 294px; top: 20px; width: 96px; height: 96px; }
  .back-mark__name { position: absolute; left: 0; right: 0; top: 30px; text-align: center;
    font-family: "Cabin", sans-serif; font-weight: 600; font-size: 15px; line-height: 1.1; color: var(--ink-soft); }
  .stamp-box { position: absolute; left: 418px; top: 29px; width: 108px; height: 108px; border: 1.5px solid var(--rule); }
  .return-address { position: absolute; left: 404px; top: 141px; width: 136px; text-align: center;
    font-family: Arial, Helvetica, sans-serif; font-size: 11px; line-height: 13px; color: #111; }
  .address-line { position: absolute; left: 313px; width: 213px; height: 1px; background: var(--rule); }
</style>
</head>
<body>

  <section class="card card--front" aria-label="Postcard front">
    <div class="flower-strip" role="img" aria-label="Photograph of orange roses and purple stock flowers"></div>

    <div class="opening-banner">
      <svg width="420" height="100" viewBox="0 0 420 100" aria-hidden="true">
        <ellipse cx="210" cy="50" rx="208" ry="48" fill="var(--slate)"/>
        <ellipse cx="210" cy="46" rx="196" ry="40" fill="var(--orange)"/>
      </svg>
      <h1 class="opening-banner__title">Grand Opening</h1>
      <p class="opening-banner__date">December 25, 2014</p>
    </div>

    <p class="tagline">Unforgettable nontraditional flower arrangements</p>

    <div class="brand-mark">
      <svg width="190" height="190" viewBox="0 0 190 190" aria-hidden="true">
        <circle cx="95" cy="95" r="88" fill="#f4efd6" stroke="var(--slate)" stroke-width="3"/>
      </svg>
      <p class="brand-mark__name">Hollow Briar<br>Flower Shop</p>
    </div>

    <p class="service-note">Now serving Cedar Bend<br>for all your floral needs</p>

    <div class="gift-offer">
      <span class="gift-offer__lead">FREE GIFT</span>
      with any in store purchase
    </div>

    <p class="phone">
      <svg width="20" height="20" viewBox="0 0 20 20" aria-hidden="true">
        <circle cx="10" cy="10" r="8.5" fill="none" stroke="var(--rose-red)" stroke-width="1.6"/>
        <path d="M7 5.5c-1 .8-1.3 2.3-.4 4.2s2.6 3.8 4.4 4.6c1.2.5 2 .3 2.6-.3l-1.6-1.8-1.2.6c-1-.5-2-1.6-2.5-2.6l.6-1.2z" fill="var(--rose-red)"/>
      </svg>
      337 555 0148
    </p>

    <p class="web-band">www.hollowbriarflowers.com</p>
  </section>

  <section class="card card--back" aria-label="Postcard back">
    <div class="offer-panel">
      <p class="offer-panel__intro">Flowers for all occasions, event planning, and-one-of-a-kind home décor items</p>
      <div class="products">
        <p>Our Products:</p>
        <ul class="products__list">
          <li>Dozen Roses</li>
          <li>Funeral Flowers</li>
          <li>Balloon Bouquets</li>
          <li>Fresh Flowers</li>
          <li>Green/House Plants</li>
          <li>Fruit/Gourmet Gift Baskets</li>
        </ul>
      </div>

      <div class="delivery-heart">
        <svg width="112" height="86" viewBox="0 0 112 86" aria-hidden="true">
          <path d="M56 85 C30 68 2 50 2 25 C2 10 14 1 28 1 C42 1 51 9 56 17 C61 9 70 1 84 1 C98 1 110 10 110 25 C110 50 82 68 56 85 Z" fill="var(--rose-red)"/>
        </svg>
        <p class="delivery-heart__text"><strong>FREE</strong>LOCAL DELIVERY For the First 30 customers to present this card</p>
      </div>
      <p class="frequent-program">Join our<br>FREQUENT FLOWER<br>PROGRAM</p>

      <div class="happy-hour">Special FLower<br>HAPPY HOUR<br>Each Day<br>A Week</div>
      <p class="rose-promo">Watch Out For<br>ROSES FOR A MONTH<br>Promotion</p>
    </div>

    <div class="back-mark">
      <svg width="96" height="96" viewBox="0 0 96 96" aria-hidden="true">
        <circle cx="48" cy="48" r="44" fill="#f4efd6" stroke="var(--slate)" stroke-width="2"/>
      </svg>
      <p class="back-mark__name">Hollow Briar<br>Flower Shop</p>
    </div>

    <div class="stamp-box" aria-label="Postage area"></div>
    <p class="return-address">418 Magnolia Lane<br>Suite C<br>Cedar Bend<br>Louisiana 70512</p>

    <div class="address-line" style="top:210px"></div>
    <div class="address-line" style="top:242px"></div>
    <div class="address-line" style="top:274px"></div>
    <div class="address-line" style="top:305px"></div>
  </section>

</body>
</html>
```